Social News web page design website name Vorlet.

I need a web design for a start up project called Vorlet based in Sydney. Its a social news website. it helps people to get centralized news and people can have their own profiles where they can post there thoughts and comments and it will be free to signup and usage as well.

I would like to see designs that use the latest pelican scaffold framework and are mobile compatible. only need 2 pages a home page kind of similar to
plonk (http://plonk.example/) and a profile that's a next gen user profile page I will leave that to you imaginations

this is my previous design I did on my own http://www.vorlet.example/

Target Market(s)

target market is 13 and up and anyone who likes or uses social media and would be able to understand the site

Industry/Entity Type

News

Requirements
Must have
• 1.) using pelican scaffold. 2) a home page similar to plonk (http://plonk.example/) or even better free to use your imagination 3) a next gen profile page better the one i made on my own which is this one (http://www.vorlet.example/profile/hollisbrackett) 4) for mobile navigation, have a mobile navigation something similar to http://slidepanel.quenrow.example/
Nice to have
• 1) a sexy navigation and layout for both desktop and mobile phones. i will leave that to you imaginations. 2) social medial buttons like to sign-in with and also to post a story to Chatterly or pelican 3) a user settings page (but not necessary) 4) a login or signup (but not necessary)

```html
<!DOCTYPE html>
<html lang="en">
<head>
<meta charset="utf-8">
<title>Vorlet — Social News</title>
<link href="https://fonts.googleapis.com/css2?family=Open+Sans:wght@400;600;700&family=Arimo:wght@400;700&display=swap" rel="stylesheet">
<style>
:root{
  --page:#f6f6f6;
  --card:#ffffff;
  --ink:#1e1e1e;
  --text:#3a3a3a;
  --muted:#8d8d8d;
  --rule:#2b2b2b;
  --hair:#d6d6d6;
  --panel:#f4f2ee;
  --green:#4b9a3a;
  --icon:#9a9a9a;
}
*{box-sizing:border-box;margin:0;padding:0}
html,body{width:852px;height:1200px;overflow:hidden}
body{background:var(--page);font-family:"Arimo",Arial,sans-serif;color:var(--text);position:relative}
.sheet{position:absolute;left:67px;top:15px;width:714px;height:1162px;background:var(--card);box-shadow:0 0 3px rgba(0,0,0,.08)}
.brand{position:absolute;left:89px;top:30px;font-family:"Open Sans",sans-serif;font-weight:700;font-size:24px;color:var(--ink);letter-spacing:-.3px}
.social-box{position:absolute;left:683px;top:35px;width:74px;height:22px;background:#eeeeee;border-radius:3px;display:flex;align-items:center;justify-content:center;gap:7px}
.dot{width:8px;height:8px;border-radius:50%;background:var(--icon)}
.main-nav{position:absolute;left:89px;top:76px;width:668px;height:30px;border-top:3px solid var(--rule);border-bottom:1px solid var(--hair);display:flex;align-items:center;font-family:"Open Sans",sans-serif;font-size:9px;font-weight:600;color:var(--ink)}
.main-nav a{color:inherit;text-decoration:none;padding:0 12px;border-left:1px solid var(--hair);line-height:10px}
.main-nav a:first-child{border-left:none;padding-left:12px}
.hero{position:absolute;left:89px;top:123px;width:666px;height:305px;display:flex}
.hero-media{position:relative;width:462px;height:305px;background:linear-gradient(160deg,#e6eaee 0%,#c9d0d6 45%,#8f9297 70%,#b7bec5 100%)}
.expand{position:absolute;right:7px;top:7px;width:18px;height:18px;background:#9c9c9c;border-radius:2px;opacity:.8}
.hero-next{position:absolute;right:12px;top:143px}
.hero-panel{flex:1;background:var(--panel);padding:14px 13px;position:relative}
.story-nav{display:flex;justify-content:space-between;align-items:center;font-size:7.5px;line-height:9px;color:var(--ink);font-family:"Open Sans",sans-serif}
.story-link{display:flex;align-items:center;gap:5px}
.grid-icon{display:grid;grid-template-columns:5px 5px;gap:2px}
.grid-icon i{display:block;width:5px;height:5px;background:#333}
.hero-title{margin-top:24px;font-size:14px;font-weight:700;color:var(--ink)}
.hero-text{margin-top:9px;width:176px;font-size:9.6px;line-height:15.7px;color:var(--muted);hyphens:auto;-webkit-hyphens:auto}
.hero-share{position:absolute;left:13px;bottom:14px;display:flex;gap:6px}
.hero-share .dot{width:7px;height:7px}
.strip{position:absolute;left:91px;width:663px}
.strip-head{border-top:3px solid var(--rule);border-bottom:1px dotted #b5b5b5;height:27px;display:flex;justify-content:space-between;align-items:center;padding:0 8px 0 2px}
.strip-head h2{font-size:8.5px;font-weight:700;color:var(--ink)}
.pager{display:flex;gap:8px}
.cards{display:grid;grid-template-columns:repeat(4,147px);column-gap:23px;padding:13px 0 0 3px}
.story-card{box-shadow:0 1px 2px rgba(0,0,0,.1);height:225px}
.thumb{height:104px}
.story-body{padding:12px 10px 0}
.story-title{font-size:8.3px;font-weight:700;color:var(--ink)}
.story-cat{margin-top:8px;font-size:7.3px;color:var(--green);letter-spacing:.3px}
.story-text{margin-top:12px;font-size:7.7px;line-height:13.6px;color:#666;text-align:justify}
.story-share{margin-top:5px;display:flex;gap:9px;font-size:8.5px;color:#666}
.story-share span{display:flex;align-items:center;gap:3px}
.sq{width:7px;height:7px;background:#666}
.ci{width:7px;height:7px;background:#666;border-radius:50%}
.video{height:85px;position:relative}
.video svg{position:absolute;left:8px;bottom:12px}
.copyright{position:absolute;left:68px;top:1185px;font-size:8.5px;color:#555}
</style>
</head>
<body>
<div class="sheet"></div>
<div class="brand">Vorlet</div>
<div class="social-box"><span class="dot"></span><span class="dot"></span><span class="dot"></span><span class="dot"></span></div>

<nav class="main-nav">
  <a href="#">HOME</a><a href="#">VIDEO</a><a href="#">READER</a><a href="#">SUBMIT STORY</a><a href="#">ADVERTISE</a>
</nav>

<section class="hero">
  <div class="hero-media" role="img" aria-label="Feature photo: an old tank tipping off a barge into grey sea water">
    <span class="expand"></span>
    <svg class="hero-next" width="10" height="16" viewBox="0 0 10 16"><path d="M2 2l6 6-6 6" fill="none" stroke="#222" stroke-width="2"/></svg>
  </div>
  <div class="hero-panel">
    <div class="story-nav">
      <div class="story-link"><svg width="7" height="12" viewBox="0 0 7 12"><path d="M6 1L1 6l5 5" fill="none" stroke="#222" stroke-width="1.8"/></svg><span>PREV<br>STORY</span></div>
      <div class="grid-icon"><i></i><i></i><i></i><i></i></div>
      <div class="story-link" style="text-align:right"><span>NEXT<br>STORY</span><svg width="7" height="12" viewBox="0 0 7 12"><path d="M1 1l5 5-5 5" fill="none" stroke="#222" stroke-width="1.8"/></svg></div>
    </div>
    <h1 class="hero-title">All Along The Watchtower</h1>
    <p class="hero-text">We all know basic tenets of user-centered design. We recognize different research methods, the prototyping stage, as well as the process of documenting techniques in our rich methodological environment. The question you probably often ask yourself, though, is how it all works in practice?</p>
    <div class="hero-share"><span class="dot"></span><span class="dot"></span><span class="dot"></span><span class="dot"></span></div>
  </div>
</section>

<section class="strip" style="top:464px">
  <div class="strip-head"><h2>More Story</h2><div class="pager"><svg width="6" height="10" viewBox="0 0 6 10"><path d="M5 1L1 5l4 4" fill="none" stroke="#222" stroke-width="1.6"/></svg><svg width="6" height="10" viewBox="0 0 6 10"><path d="M1 1l4 4-4 4" fill="none" stroke="#222" stroke-width="1.6"/></svg></div></div>
  <div class="cards">
    <article class="story-card"><div class="thumb" role="img" aria-label="Photo of a politician in a suit at a podium" style="background:linear-gradient(90deg,#7a1a16,#2a2a2a 60%,#c8c0b4)"></div><div class="story-body"><h3 class="story-title">THIS IS THE TITLE</h3><p class="story-cat">CATEGORY</p><p class="story-text">In a move that is rare, bizarre, and embarrassing, the Council has revoked an Aurel nomina-</p><p class="story-share"><span><i class="sq"></i>Chatterly</span><span><i class="ci"></i>Pelican</span></p></div></article>
    <article class="story-card"><div class="thumb" role="img" aria-label="Film still of two people face to face" style="background:linear-gradient(90deg,#2a1c18,#6b4a3e 50%,#1c1616)"></div><div class="story-body"><h3 class="story-title">THIS IS THE TITLE</h3><p class="story-cat">CATEGORY</p><p class="story-text">In a move that is rare, bizarre, and embarrassing, the Council has revoked an Aurel nomina-</p><p class="story-share"><span><i class="sq"></i>Chatterly</span><span><i class="ci"></i>Pelican</span></p></div></article>
    <article class="story-card"><div class="thumb" role="img" aria-label="Portrait photo against a starry red background" style="background:radial-gradient(circle at 20% 20%,#f0d2b0,#8a3a2e 45%,#2a1616)"></div><div class="story-body"><h3 class="story-title">THIS IS THE TITLE</h3><p class="story-cat">CATEGORY</p><p class="story-text">In a move that is rare, bizarre, and embarrassing, the Council has revoked an Aurel nomina-</p><p class="story-share"><span><i class="sq"></i>Chatterly</span><span><i class="ci"></i>Pelican</span></p></div></article>
    <article class="story-card"><div class="thumb" role="img" aria-label="Football players in a game" style="background:linear-gradient(135deg,#3a4a6a,#7a7f8c 50%,#c9c2b0)"></div><div class="story-body"><h3 class="story-title">THIS IS THE TITLE</h3><p class="story-cat">CATEGORY</p><p class="story-text">In a move that is rare, bizarre, and embarrassing, the Council has revoked an Aurel nomina-</p><p class="story-share"><span><i class="sq"></i>Chatterly</span><span><i class="ci"></i>Pelican</span></p></div></article>
  </div>
</section>

<section class="strip" style="top:748px">
  <div class="strip-head"><h2>Upcoming Story</h2><div class="pager"><svg width="6" height="10" viewBox="0 0 6 10"><path d="M5 1L1 5l4 4" fill="none" stroke="#222" stroke-width="1.6"/></svg><svg width="6" height="10" viewBox="0 0 6 10"><path d="M1 1l4 4-4 4" fill="none" stroke="#222" stroke-width="1.6"/></svg></div></div>
  <div class="cards">
    <article class="story-card"><div class="thumb" role="img" aria-label="Sports show title card with a puppet host" style="background:linear-gradient(135deg,#1a3560,#123058 55%,#a31c1c)"></div><div class="story-body"><h3 class="story-title">THIS IS THE TITLE</h3><p class="story-cat">CATEGORY</p><p class="story-text">In a move that is rare, bizarre, and embarrassing, the Council has revoked an Aurel nomina-</p><p class="story-share"><span><i class="sq"></i>Chatterly</span><span><i class="ci"></i>Pelican</span></p></div></article>
    <article class="story-card"><div class="thumb" role="img" aria-label="Group of ice skaters in colourful costumes" style="background:linear-gradient(180deg,#f6f6f8,#e4e8ee 60%,#c8d6e4)"></div><div class="story-body"><h3 class="story-title">THIS IS THE TITLE</h3><p class="story-cat">CATEGORY</p><p class="story-text">In a move that is rare, bizarre, and embarrassing, the Council has revoked an Aurel nomina-</p><p class="story-share"><span><i class="sq"></i>Chatterly</span><span><i class="ci"></i>Pelican</span></p></div></article>
    <article class="story-card"><div class="thumb" role="img" aria-label="People resting in an airport lounge under red arches" style="background:linear-gradient(135deg,#3a3a3a,#9a2418 40%,#5a5a5a)"></div><div class="story-body"><h3 class="story-title">THIS IS THE TITLE</h3><p class="story-cat">CATEGORY</p><p class="story-text">In a move that is rare, bizarre, and embarrassing, the Council has revoked an Aurel nomina-</p><p class="story-share"><span><i class="sq"></i>Chatterly</span><span><i class="ci"></i>Pelican</span></p></div></article>
    <article class="story-card"><div class="thumb" role="img" aria-label="Red brick apartment building" style="background:linear-gradient(90deg,#7a3a30,#9a5044 60%,#d6d8d4)"></div><div class="story-body"><h3 class="story-title">THIS IS THE TITLE</h3><p class="story-cat">CATEGORY</p><p class="story-text">In a move that is rare, bizarre, and embarrassing, the Council has revoked an Aurel nomina-</p><p class="story-share"><span><i class="sq"></i>Chatterly</span><span><i class="ci"></i>Pelican</span></p></div></article>
  </div>
</section>

<section class="strip" style="top:1033px">
  <div class="strip-head"><h2>Videos</h2><div class="pager"><svg width="6" height="10" viewBox="0 0 6 10"><path d="M5 1L1 5l4 4" fill="none" stroke="#222" stroke-width="1.6"/></svg><svg width="6" height="10" viewBox="0 0 6 10"><path d="M1 1l4 4-4 4" fill="none" stroke="#222" stroke-width="1.6"/></svg></div></div>
  <div class="cards">
    <div class="video" role="img" aria-label="Video still of a horse in a room" style="background:linear-gradient(135deg,#8a8e92,#3a3836 55%,#6a6660)"><svg width="12" height="12" viewBox="0 0 12 12"><path d="M1 0l11 6-11 6z" fill="#fff"/></svg></div>
    <div class="video" role="img" aria-label="Video still of a tattooed fist" style="background:radial-gradient(circle at 55% 50%,#b08878,#4a4a4a 70%)"><svg width="12" height="12" viewBox="0 0 12 12"><path d="M1 0l11 6-11 6z" fill="#fff"/></svg></div>
    <div class="video" role="img" aria-label="Sitcom scene in a bedroom" style="background:linear-gradient(135deg,#2a3a5a,#6a5a4a 55%,#3a2e28)"><svg width="12" height="12" viewBox="0 0 12 12"><path d="M1 0l11 6-11 6z" fill="#fff"/></svg></div>
    <div class="video" role="img" aria-label="Video still of a horse in a room" style="background:linear-gradient(135deg,#8a8e92,#3a3836 55%,#6a6660)"><svg width="12" height="12" viewBox="0 0 12 12"><path d="M1 0l11 6-11 6z" fill="#fff"/></svg></div>
  </div>
</section>

<p class="copyright">© Copyright Vorlet</p>
</body>
</html>
```